Dog Grooming Provisions - Coat Revival Mist *

We are Moss Hollow Meadows. A city dog's country camp. We are a dog services company providing a camp experience in Upstate NY to the dogs of NYC. We are creating a hand made Coat Revival Mist for our clients (who are dogs!) for the holidays.
These labels will be used on a 4 ounce vintage style spray bottles. The design should have a vintage grooming provisions feel. We'd like to see the design be a simple, vintage style black with white, charcoal, or very dark almost black green.
The design should incorporate our varying vintage fonts, our logo with "grooming provisions" all natural & handmade, Coat Revive
Obviously this is a gift and while Coat Revive is important, our brand should be a focus. Perhaps a very simple and "elegant" bone but steer away from paws and pet cheesy! Classic, vintage and camp.

Target Market(s)

Upscale Pet Owners of NYC

Industry/Entity Type

Pet Care

Logo Text

Moss Hollow Meadows Dog Camp (Dog Camp is is for logo not necessary for label)

Font styles to use
Serif
Sans Serif
Script

Colors
9bcb3b
000000
5c5c5c

Requirements
Must have
• I am looking for a black and white or very simple design. I'd even like our logo for this use be black/white (if possible? - not sure if that can happen?)
• Our branding! Simple vintage feel.
• Grooming Provisions
• Coat Revival or Coat Revive or Coat Bright Mist
• Handmade
• All Natural
• Fonts of vintage style - varying with simple and bold (i attached some photos)
Nice to have
• **MAYBE a very Simple Bone (see drawing) - very very thin.
Should not have
• 1. PAWS or cheap looking dog related items
• 2. No bright colors - truly prefer black and white or black with intention to print on plain pulp/brown paper (attached photo)
• 3. Over designed

```html
<!DOCTYPE html>
<html lang="en">
<head>
<meta charset="utf-8">
<title>Moss Hollow Meadows – Coat Revival Label</title>
<link rel="stylesheet" href="https://fonts.googleapis.com/css2?family=Barlow:wght@400;500&family=Dancing+Script:wght@500&family=Rubik:wght@800&display=swap">
<style>
  :root {
    --page: #ffffff;
    --sage: #b3c8ba;
    --charcoal: #2e2c2d;
    --ridge: #363334;
    --frame-line: #c6d2ca;
    --ink: #ffffff;
  }
  html, body {
    margin: 0;
    padding: 0;
    width: 1162px;
    height: 1200px;
    overflow: hidden;
    background: var(--page);
  }
  .label {
    position: relative;
    width: 1162px;
    height: 1200px;
  }
  .label-shape {
    position: absolute;
    inset: 0;
  }
  .brand-mark {
    position: absolute;
    left: 381px;
    top: 250px;
    width: 400px;
    text-align: center;
  }
  .brand-mark__dot {
    display: block;
    width: 84px;
    height: 84px;
    margin: 0 auto 22px;
    border-radius: 50%;
    background: var(--sage);
  }
  .brand-mark__name {
    font-family: "Barlow", sans-serif;
    font-weight: 500;
    font-size: 34px;
    line-height: 1.15;
    color: var(--sage);
  }
  .text-line {
    position: absolute;
    left: 0;
    width: 1162px;
    text-align: center;
    color: var(--ink);
    margin: 0;
    line-height: 1.2;
  }
  .category {
    top: 536px;
    font-family: "Barlow", sans-serif;
    font-weight: 400;
    font-size: 39px;
  }
  .brand-script {
    top: 604px;
    font-family: "Dancing Script", cursive;
    font-weight: 500;
    font-size: 76px;
  }
  .product-name {
    top: 724px;
    font-family: "Rubik", sans-serif;
    font-weight: 800;
    font-size: 100px;
    letter-spacing: 1px;
  }
  .qualities {
    top: 876px;
    font-family: "Dancing Script", cursive;
    font-weight: 500;
    font-size: 52px;
  }
  .established {
    top: 962px;
    font-family: "Barlow", sans-serif;
    font-weight: 400;
    font-size: 36px;
  }
</style>
</head>
<body>
<main class="label">
  <svg class="label-shape" width="1162" height="1200" viewBox="0 0 1162 1200" aria-hidden="true">
    <defs>
      <linearGradient id="ridge-fade" x1="0" y1="0" x2="0" y2="1">
        <stop offset="0" stop-color="var(--charcoal)"/>
        <stop offset="0.4" stop-color="var(--ridge)"/>
        <stop offset="1" stop-color="var(--charcoal)"/>
      </linearGradient>
    </defs>
    <path fill="var(--sage)" d="M209 105 H965 A44 44 0 0 0 1009 149 V1062 A44 44 0 0 0 965 1106 H209 A44 44 0 0 0 165 1062 V149 A44 44 0 0 0 209 105 Z"/>
    <path fill="var(--charcoal)" d="M215 115 H959 A40 40 0 0 0 999 155 V1056 A40 40 0 0 0 959 1096 H215 A40 40 0 0 0 175 1056 V155 A40 40 0 0 0 215 115 Z"/>
    <path fill="none" stroke="var(--frame-line)" stroke-width="1.5" d="M236 145 H938 A30 30 0 0 0 968 175 V1035 A30 30 0 0 0 938 1065 H236 A30 30 0 0 0 206 1035 V175 A30 30 0 0 0 236 145 Z"/>
    <line x1="252" y1="712" x2="920" y2="712" stroke="var(--frame-line)" stroke-width="2.5"/>
    <line x1="252" y1="862" x2="920" y2="862" stroke="var(--frame-line)" stroke-width="2.5"/>
  </svg>

  <svg class="label-shape" width="1162" height="1200" viewBox="0 0 1162 1200" role="img" aria-label="Faint mountain range backdrop behind the brand mark">
    <rect x="207" y="285" width="760" height="160" fill="url(#ridge-fade)"/>
  </svg>

  <div class="brand-mark">
    <span class="brand-mark__dot"></span>
    <span class="brand-mark__name">Moss Hollow Meadows</span>
  </div>

  <p class="text-line category">Grooming • Provisions</p>
  <p class="text-line brand-script">Moss Hollow Meadows</p>
  <h1 class="text-line product-name">Coat Revival</h1>
  <p class="text-line qualities">hand made | all natural</p>
  <p class="text-line established">*est 2005*</p>
</main>
</body>
</html>
```